LOGO DESIGN: Construction Related Service Business

We require a logo for our business Dovtar Services. We are a construction related business offering a range of services including machine services for groundworks (digging trenches, soak wells, preparing land for construction etc), demolition and truck haulage from demolition sites.
We would like our logo to be predominately text, but may include abstract graphics. The colour scheme should be mainly a mid bright blue and overall be quite 'clean'.

Industry/Entity Type

Construction

Contact Information for Business Card

Colin Pruett
Ph:041 562 9083
dovtarservices@keloran.com.au

Colors
0456a3

```html
<!DOCTYPE html>
<html lang="en">
<head>
<meta charset="utf-8">
<title>Dovtar Services — Business Card</title>
<link rel="stylesheet" href="https://fonts.googleapis.com/css2?family=Arimo:wght@400&family=Cinzel:wght@400&display=swap">
<style>
  :root {
    --navy: #07446b;
    --slate: #808184;
    --rule: #d9dbdd;
    --contact-text: #8c8f93;
  }
  html, body {
    margin: 0;
    padding: 0;
    width: 740px;
    height: 1200px;
    overflow: hidden;
    background: var(--navy);
  }
  .card {
    position: relative;
    width: 740px;
    height: 1200px;
    background: var(--navy);
  }
  .header-band {
    position: absolute;
    left: 0; top: 0;
    width: 740px; height: 281px;
    background: var(--navy);
  }
  .machine-illustration {
    position: absolute;
    left: 76px; top: 49px;
    width: 557px; height: 232px;
    background: linear-gradient(to top, #6f7a85 0%, #4b6479 100%);
    border-radius: 60px 60px 0 0;
  }
  .divider {
    position: absolute;
    left: 0;
    width: 740px;
    height: 8px;
    background: var(--rule);
  }
  .divider--top { top: 281px; }
  .divider--bottom { top: 915px; }
  .name-panel {
    position: absolute;
    left: 0; top: 289px;
    width: 740px; height: 626px;
    background: var(--slate);
  }
  .wordmark {
    position: absolute;
    left: 0; width: 740px;
    margin: 0;
    text-align: center;
    color: var(--navy);
    font-family: "Arimo", Arial, sans-serif;
    font-weight: 400;
    line-height: 1;
  }
  .wordmark__primary {
    top: 170px;
    font-size: 150px;
    letter-spacing: 1px;
  }
  .wordmark__secondary {
    top: 346px;
    font-size: 124px;
    letter-spacing: 0;
  }
  .contact {
    position: absolute;
    left: 0; top: 923px;
    width: 740px; height: 277px;
    font-family: "Cinzel", "Times New Roman", serif;
    color: var(--contact-text);
  }
  .contact__heading {
    margin: 0;
    position: absolute;
    top: 12px; left: 0; width: 740px;
    text-align: center;
    font-size: 33px;
    font-weight: 400;
    letter-spacing: 1px;
  }
  .contact__list {
    position: absolute;
    left: 45px; top: 64px;
    margin: 0; padding: 0;
    list-style: none;
    font-size: 34px;
    line-height: 44px;
    letter-spacing: 0.5px;
  }
  .contact__email {
    font-size: 31px;
    letter-spacing: 0.3px;
  }
</style>
</head>
<body>
  <div class="card">
    <div class="header-band">
      <div class="machine-illustration" role="img" aria-label="Grey silhouette of an excavator with raised boom and arm"></div>
    </div>
    <div class="divider divider--top"></div>

    <section class="name-panel">
      <h1 class="wordmark wordmark__primary">DOVTAR</h1>
      <p class="wordmark wordmark__secondary">SERVICES</p>
    </section>

    <div class="divider divider--bottom"></div>

    <section class="contact">
      <h2 class="contact__heading">Contact Information</h2>
      <ul class="contact__list">
        <li class="contact__name">Colin Pruett</li>
        <li class="contact__phone">Phone: 041 562 9083</li>
        <li class="contact__email">dovtarservices@keloran.com.au</li>
      </ul>
    </section>
  </div>
</body>
</html>
```